LETTERHEAD & ENVELOPE: eye-catching stationary design for our custom office furniture business

Our company recently rebranded and we are in need of new stationary. Specifically, we need branded letterhead for standard paper size (8.5” x 11”), and matching envelopes, size: #9.

All designs should incorporate our brand colors, brand typeface, and logo. Please view attached brand guidelines document for brand colors, and brand description.

Letterhead: 8.5” x 11” Must include CoralvexKTN Logo, Dorrit Falke Certified Dealer Logo, mailing address, phone number, website, and email address.

Envelope: 9.5” x 4.125” Must include CoralvexKTN Logo, mailing address, and Dorrit Falke Certified Dealer Logo.

Attached files include:

```html
<!DOCTYPE html>
<html lang="en">
<head>
<meta charset="utf-8">
<title>CoralvexKTN Stationery</title>
<link rel="stylesheet" href="https://fonts.googleapis.com/css2?family=Raleway:wght@400;500&family=Roboto+Condensed:wght@300;500&display=swap">
<style>
  :root {
    --backdrop: #d6d6d6;
    --paper: #ededed;
    --brand-green: #668577;
    --watermark: #d9dedc;
    --white: #ffffff;
    --rule: #6f8a7e;
  }
  * { margin: 0; padding: 0; box-sizing: border-box; }
  html, body { width: 1200px; height: 840px; overflow: hidden; }
  body {
    background: var(--backdrop);
    font-family: "Raleway", sans-serif;
    position: relative;
  }

  /* Letterhead */
  .letterhead {
    position: absolute; left: 169px; top: 138px;
    width: 435px; height: 561px;
    background: var(--paper);
    overflow: hidden;
  }
  .letterhead .brand {
    position: absolute; top: 30px; left: 0; right: 0;
    display: flex; justify-content: center; align-items: center; gap: 8px;
    color: var(--brand-green);
  }
  .brand-dot {
    width: 27px; height: 27px; border-radius: 50%;
    background: var(--brand-green);
  }
  .brand-name { font-size: 20px; font-weight: 400; letter-spacing: 0.2px; }
  .letterhead .watermark {
    position: absolute; left: -60px; top: 150px;
    width: 290px; height: 290px; border-radius: 50%;
    background: var(--watermark);
  }
  .letterhead .footer-rule {
    position: absolute; left: 29px; right: 29px; top: 505px;
    border-top: 1px solid var(--rule);
  }
  .contact-row {
    position: absolute; left: 28px; right: 29px; top: 516px;
    display: flex; justify-content: space-between; align-items: center;
    color: var(--brand-green);
    font-size: 5.6px; font-weight: 500; letter-spacing: 0.1px;
    text-transform: uppercase; line-height: 1.25;
  }
  .contact-item { display: flex; align-items: center; gap: 6px; }
  .contact-icon { width: 13px; height: 13px; flex: none; }

  /* Envelope back */
  .envelope-back {
    position: absolute; left: 628px; top: 236px;
    width: 340px; height: 170px;
    background: var(--brand-green);
    overflow: hidden;
  }
  .envelope-back .flap { position: absolute; left: 0; top: 0; width: 340px; height: 51px; }
  .envelope-back .brand {
    position: absolute; top: 80px; left: 0; right: 0;
    display: flex; justify-content: center; align-items: center; gap: 8px;
    color: var(--white);
  }
  .envelope-back .brand-dot { width: 28px; height: 28px; background: var(--white); }
  .envelope-back .brand-name { font-size: 21px; }

  /* Envelope front */
  .envelope-front {
    position: absolute; left: 682px; top: 435px;
    width: 385px; height: 166px;
    background: var(--brand-green);
    overflow: hidden;
  }
  .envelope-front .mark-circle {
    position: absolute; left: -40px; top: 48px;
    width: 170px; height: 170px; border-radius: 50%;
    background: var(--white);
  }
  .dealer {
    position: absolute; left: 251px; top: 114px;
    display: flex; align-items: center; gap: 6px;
    color: var(--white);
    font-family: "Roboto Condensed", sans-serif;
    font-size: 7.6px; font-weight: 300;
  }
  .dealer-badge { width: 15px; height: 15px; border-radius: 50%; background: var(--white); }
  .dealer strong { font-weight: 500; }
  .return-address {
    position: absolute; left: 252px; top: 137px;
    display: flex; align-items: center; gap: 8px;
    color: var(--white);
    font-size: 4.6px; font-weight: 500; text-transform: uppercase; line-height: 1.25;
  }
  .return-address .contact-icon { width: 12px; height: 12px; }
</style>
</head>
<body>

  <section class="letterhead" aria-label="Letterhead">
    <div class="brand">
      <span class="brand-dot"></span>
      <span class="brand-name">CoralvexKTN</span>
    </div>
    <div class="watermark"></div>
    <div class="footer-rule"></div>
    <div class="contact-row">
      <div class="contact-item">
        <svg class="contact-icon" viewBox="0 0 20 20"><circle cx="10" cy="10" r="10" fill="#668577"/><path d="M10 4.5a3.6 3.6 0 0 0-3.6 3.6c0 2.7 3.6 6.8 3.6 6.8s3.6-4.1 3.6-6.8A3.6 3.6 0 0 0 10 4.5z" fill="#fff"/><circle cx="10" cy="8.1" r="1.3" fill="#668577"/></svg>
        <span>418 NE Larkspur, Suite 140<br>Portland, OR 97210</span>
      </div>
      <div class="contact-item">
        <svg class="contact-icon" viewBox="0 0 20 20"><circle cx="10" cy="10" r="10" fill="#668577"/><circle cx="10" cy="10" r="5.5" fill="none" stroke="#fff" stroke-width="1.2"/><path d="M4.5 10h11M10 4.5c-2.4 3-2.4 8 0 11M10 4.5c2.4 3 2.4 8 0 11" fill="none" stroke="#fff" stroke-width="1"/></svg>
        <span>www.coralvexktn.com</span>
      </div>
      <div class="contact-item">
        <svg class="contact-icon" viewBox="0 0 20 20"><circle cx="10" cy="10" r="10" fill="#668577"/><rect x="5" y="6.5" width="10" height="7" rx="0.8" fill="#fff"/><path d="M5.3 7l4.7 3.6L14.7 7" fill="none" stroke="#668577" stroke-width="1"/></svg>
        <span>info@coralvexktn.com</span>
      </div>
      <div class="contact-item">
        <svg class="contact-icon" viewBox="0 0 20 20"><circle cx="10" cy="10" r="10" fill="#668577"/><path d="M7 5.2l1.7-.3 1 2.5-1.2 1a6 6 0 0 0 3 3l1-1.2 2.5 1-.3 1.7c-.2.8-1 1.2-1.8 1C9.6 13.4 6.6 10.4 6 7c-.2-.8.2-1.6 1-1.8z" fill="#fff"/></svg>
        <span>555.014.2290</span>
      </div>
    </div>
  </section>

  <section class="envelope-back" aria-label="Envelope back">
    <svg class="flap" viewBox="0 0 340 51" preserveAspectRatio="none"><path d="M0 0H340L326 41Q323 49 314 49H26Q17 49 14 41Z" fill="#ededed"/></svg>
    <div class="brand">
      <span class="brand-dot"></span>
      <span class="brand-name">CoralvexKTN</span>
    </div>
  </section>

  <section class="envelope-front" aria-label="Envelope front">
    <div class="mark-circle"></div>
    <div class="dealer">
      <span class="dealer-badge"></span>
      <span><strong>Dorrit Falke</strong> Certified Dealer</span>
    </div>
    <div class="return-address">
      <svg class="contact-icon" viewBox="0 0 20 20"><circle cx="10" cy="10" r="10" fill="#fff"/><path d="M10 4.5a3.6 3.6 0 0 0-3.6 3.6c0 2.7 3.6 6.8 3.6 6.8s3.6-4.1 3.6-6.8A3.6 3.6 0 0 0 10 4.5z" fill="#668577"/><circle cx="10" cy="8.1" r="1.3" fill="#fff"/></svg>
      <span>418 NE Larkspur, Suite 140<br>Portland, OR 97210</span>
    </div>
  </section>

</body>
</html>
```